SKYWARD LENSWORKS New Wordpress Design Project

Skyward Lensworks is a photo-sharing site for aviation photographers and enthusiasts.

Please redesign the home page (http://www.skywardlensworks.example/) and photo feature page (http://www.skywardlensworks.example/2014/10/borvel-freight-23/).

We like and would like to keep the logo we have, but are open to changing colors on the logo to suit a new color scheme if necessary.
Updates

Hi All, Thank you for taking part in this design competition. Could you please show us your first round design concepts within 24hrs as we hope to show our client them and start providing feedback? Much appreciated, Lex VH BramblePeak Design

Hi All, A few tips: Could you try keep the search bar above the fold Include a section for showing new blog posts Try to integrate an ads a little better also above and below the fold Appreciated, Lex Vh

Target Market(s)

Aviation photographers and enthusiasts of all age groups globally.

Industry/Entity Type

Aviation

Requirements
Must have
• • Clean and consistent layout
• A good way to incorporate advertisements on the home page and photo feature page
• Clear and simple menu navigation
• On home page – call to action to register
• On home page - call to action to upload photos
• On home page – social buttons call to action to follow, circle, like, etc
• On photo feature page – call to action to tweet, +1, Like, etc a photo
Nice to have
• Sites we like

www.quillpane.example
http://www.layoutorchard.example/demo/45176.html
Should not have
• • Unnecessary animations
• No Adobe Flash
• Overly crowded / busy design

```html
<!DOCTYPE html>
<html lang="en">
<head>
<meta charset="utf-8">
<title>Skyward Lensworks – Home</title>
<link rel="stylesheet" href="https://fonts.googleapis.com/css2?family=Open+Sans:wght@400;600;700&display=swap">
<style>
:root{
  --accent:#d9512c;
  --accent-dark:#b83f1f;
  --amber:#ef8a18;
  --amber-dark:#c96f0c;
  --ink:#1b1b1b;
  --body:#555;
  --muted:#888;
  --line:#bdbdbd;
  --band:#f0f0f0;
  --footer:#363636;
  --white:#fff;
}
*{box-sizing:border-box;margin:0;padding:0}
html,body{width:1200px;height:2687px;overflow:hidden}
body{position:relative;background:var(--white);font-family:Arial,Helvetica,sans-serif;color:var(--body)}
.abs{position:absolute}
.head-font{font-family:"Open Sans",Arial,sans-serif}

/* hero */
.hero{left:0;top:0;width:1200px;height:681px;
  background:linear-gradient(180deg,#3a4658 0%,#5a6070 25%,#8a7350 48%,#6b6a6c 62%,#2c3a4c 80%,#1d242c 100%)}
.hero-shade{left:0;top:0;width:1200px;height:681px;background:linear-gradient(180deg,rgba(0,0,0,.25),rgba(0,0,0,0) 30%,rgba(0,0,0,.25))}
.logo{left:40px;top:54px;font-family:"Open Sans",Arial,sans-serif;font-weight:700;font-size:27px;color:var(--white);letter-spacing:-.3px}
.nav a{position:absolute;top:70px;font-family:"Open Sans",Arial,sans-serif;font-size:11.5px;font-weight:600;color:var(--white);text-decoration:none;letter-spacing:.2px}
.nav-box{top:62px!important;height:30px;border:1.5px solid rgba(255,255,255,.85);border-radius:2px;text-align:center;line-height:27px;font-size:10.5px!important}
.hero-arrow{top:320px;width:16px;height:40px}
.hero-title{left:0;top:404px;width:1200px;text-align:center;font-family:"Open Sans",Arial,sans-serif;font-weight:700;font-size:34px;color:var(--white)}
.hero-sub{left:220px;top:452px;width:760px;text-align:center;font-family:"Open Sans",Arial,sans-serif;font-size:23px;line-height:35px;color:rgba(255,255,255,.92)}
.search{left:206px;top:557px;width:609px;height:43px;background:var(--white);border-radius:2px}
.search-icon{left:14px;top:13px}
.search-divider{left:44px;top:10px;width:1px;height:23px;background:#ddd}
.search-ph{left:62px;top:14px;font-size:12px;color:#aaa;font-family:"Open Sans",Arial,sans-serif}
.search-btn{left:822px;top:557px;width:172px;height:43px;background:var(--accent);color:var(--white);font-family:"Open Sans",Arial,sans-serif;font-weight:700;font-size:13px;text-align:center;line-height:43px;border-radius:2px}

/* section headings */
.sec-title{left:0;width:1200px;text-align:center;font-family:"Open Sans",Arial,sans-serif;font-weight:700;font-size:27px;color:var(--ink)}
.sec-text{text-align:center;font-size:12.5px;line-height:26px;color:var(--body)}

/* buttons */
.btn{height:59px;line-height:59px;text-align:center;color:var(--white);font-family:"Open Sans",Arial,sans-serif;font-weight:700;font-size:14px;border-radius:2px}
.btn-accent{background:var(--accent);box-shadow:0 3px 0 var(--accent-dark)}
.btn-amber{background:var(--amber);box-shadow:0 3px 0 var(--amber-dark)}
.btn-small{height:47px;line-height:47px;font-size:13px}

/* tabs */
.tab{top:1066px;height:37px;line-height:35px;text-align:center;font-family:"Open Sans",Arial,sans-serif;font-size:12px;color:#555;border:1.5px solid var(--line);background:var(--white)}
.tab-active{background:#5a5a5a;border-color:#5a5a5a;color:var(--white)}

/* photo grid */
.grid{left:0;top:1143px;width:1200px;height:351px;display:grid;grid-template-columns:repeat(5,240px);grid-template-rows:repeat(2,175.5px)}
.tile{width:100%;height:100%}

/* posts */
.post-img{top:1666px;width:214px;height:206px}
.post-title{top:1884px;width:214px;text-align:center;font-size:15px;color:var(--accent)}
.post-text{top:1914px;width:214px;text-align:center;font-size:10.5px;line-height:18px;color:#666}
.car-arrow{top:1760px}

/* ads */
.ad{top:1997px;width:287px;height:240px;border:2px solid #333}

/* about band */
.about{left:0;top:2298px;width:1200px;height:290px;background:var(--band)}

/* footer */
.footer{left:0;top:2588px;width:1200px;height:99px;background:var(--footer)}
.foot-links{left:172px;top:2615px;font-size:9.5px;color:#cfcfcf;font-family:"Open Sans",Arial,sans-serif;word-spacing:2px}
.foot-links span{margin:0 14px;color:#999}
.copy{left:172px;top:2645px;font-size:9.5px;color:#aaa;font-family:"Open Sans",Arial,sans-serif}
.social{top:2602px;width:40px;height:40px;border:1.5px solid #777;border-radius:50%}
</style>
</head>
<body>

<!-- hero -->
<div class="abs hero" role="img" aria-label="Airliner climbing over a city skyline at sunset"></div>
<div class="abs hero-shade"></div>
<div class="abs logo">Skyward Lensworks</div>
<nav class="nav">
  <a style="left:520px">HOME</a>
  <a style="left:607px">PHOTOS</a>
  <a style="left:705px">SUBMIT A PHOTO</a>
  <a style="left:856px">AIRPORT SEARCH</a>
  <a class="nav-box" style="left:980px;width:88px">LOGIN</a>
  <a class="nav-box" style="left:1077px;width:88px">REGISTER</a>
</nav>
<svg class="abs hero-arrow" style="left:66px" viewBox="0 0 16 40"><polyline points="14,2 2,20 14,38" fill="none" stroke="rgba(255,255,255,.4)" stroke-width="1.5"/></svg>
<svg class="abs hero-arrow" style="left:1118px" viewBox="0 0 16 40"><polyline points="2,2 14,20 2,38" fill="none" stroke="rgba(255,255,255,.4)" stroke-width="1.5"/></svg>
<h1 class="abs hero-title">SKYWARD LENSWORKS - ADVANCED SEARCH</h1>
<p class="abs hero-sub">It is a long established fact that a reader will be distracted by the readable content of a page when looking at its layout.</p>
<div class="abs search">
  <svg class="abs search-icon" width="16" height="16" viewBox="0 0 16 16"><circle cx="6.5" cy="6.5" r="5" fill="none" stroke="#aaa" stroke-width="1.6"/><line x1="10.2" y1="10.2" x2="14.5" y2="14.5" stroke="#aaa" stroke-width="1.8"/></svg>
  <div class="abs search-divider"></div>
  <div class="abs search-ph">AIRPORT SEARCH :</div>
</div>
<div class="abs search-btn">SEARCH NOW</div>

<!-- intro -->
<h2 class="abs sec-title" style="top:742px">SKYWARD LENSWORKS</h2>
<p class="abs sec-text" style="left:245px;top:802px;width:710px">It is a long established fact that a reader will be distracted by the readable content of a page when looking at its layout. The point of using Lorem Ipsum is that it has a more-or-less normal distribution of letters, as opposed to using 'Content here, content here', making it look like readable English.</p>
<div class="abs btn btn-accent" style="left:272px;top:922px;width:319px">REGISTER FOR SHARE A PHOTOS</div>
<div class="abs btn btn-amber" style="left:623px;top:922px;width:321px">UPLOAD A PHOTOS</div>

<!-- tabs -->
<div class="abs tab tab-active" style="left:301px;width:154px">TOP PHOTOS</div>
<div class="abs tab" style="left:471px;width:206px">MOST VIEWED TODAY</div>
<div class="abs tab" style="left:693px;width:208px">MOST VIEWED ALL TIME</div>

<!-- photo grid -->
<div class="abs grid">
  <div class="tile" role="img" aria-label="Blue helicopter on snow" style="background:linear-gradient(160deg,#cfd8e2,#2f5fb4 55%,#e9eef3)"></div>
  <div class="tile" role="img" aria-label="Jet on a wet runway at dusk" style="background:linear-gradient(180deg,#23374f,#3e5670 55%,#8a6a3e)"></div>
  <div class="tile" role="img" aria-label="Large cargo jet against blue sky" style="background:linear-gradient(180deg,#2c6fc2,#8ab6e3 60%,#eef3f8)"></div>
  <div class="tile" role="img" aria-label="Red-nosed propeller aircraft over water" style="background:linear-gradient(180deg,#6c8fce,#5f7fae 55%,#3b5680)"></div>
  <div class="tile" role="img" aria-label="Transport aircraft on a snowy apron" style="background:linear-gradient(180deg,#3b77c8,#cfd9e4 60%,#e9edf1)"></div>
  <div class="tile" role="img" aria-label="Fighter jet in blue sky" style="background:linear-gradient(180deg,#4d88cf,#a9c7e6)"></div>
  <div class="tile" role="img" aria-label="Aircraft silhouette under dark clouds" style="background:linear-gradient(180deg,#2d3a44,#6c7a80 60%,#2a3035)"></div>
  <div class="tile" role="img" aria-label="Airliner at sunset over a city" style="background:linear-gradient(180deg,#4b6b88,#e0a04a 55%,#3c3022)"></div>
  <div class="tile" role="img" aria-label="Airliner on approach over a runway under clouds" style="background:linear-gradient(180deg,#1f3d68,#c9d3dc 50%,#6d7378)"></div>
  <div class="tile" role="img" aria-label="Vintage biplane on grass" style="background:linear-gradient(180deg,#8aa8c4,#d9dee0 45%,#5d7a3b)"></div>
</div>

<!-- recent posts -->
<h2 class="abs sec-title" style="top:1543px">RECENT POSTS</h2>
<p class="abs sec-text" style="left:224px;top:1593px;width:752px">It is a long established fact that a reader will be distracted by the readable content of a page when looking at its layout. The point of using Lorem Ipsum is that it has a more-or-less normal distribution of letters...</p>
<svg class="abs car-arrow" style="left:122px" width="12" height="26" viewBox="0 0 12 26"><polyline points="10,2 2,13 10,24" fill="none" stroke="#999" stroke-width="1.5"/></svg>
<svg class="abs car-arrow" style="left:1066px" width="12" height="26" viewBox="0 0 12 26"><polyline points="2,2 10,13 2,24" fill="none" stroke="#999" stroke-width="1.5"/></svg>

<div class="abs post-img" style="left:172px;background:linear-gradient(180deg,#4a6a8a,#c9b27a 45%,#35507a)" role="img" aria-label="Airliner parked at a terminal"></div>
<div class="abs post-img" style="left:386px;background:linear-gradient(180deg,#7b8f86,#c6ced0 50%,#4d5e52)" role="img" aria-label="Business jet flying above clouds"></div>
<div class="abs post-img" style="left:600px;background:linear-gradient(180deg,#8b8b8b,#3a3a3a 55%,#2a2a2a)" role="img" aria-label="Tablet held out with a small plane above it"></div>
<div class="abs post-img" style="left:814px;background:linear-gradient(180deg,#b08a4a,#7a5a2c 50%,#2e2418)" role="img" aria-label="City skyline at dusk"></div>

<div class="abs post-title" style="left:172px">Uncover many web sites</div>
<div class="abs post-title" style="left:386px">Uncover many web sites</div>
<div class="abs post-title" style="left:600px">Uncover many web sites</div>
<div class="abs post-title" style="left:814px">Uncover many web sites</div>
<p class="abs post-text" style="left:172px">Uncover many web sites still in their infancy various versions...</p>
<p class="abs post-text" style="left:386px">Uncover many web sites still in their infancy various versions...</p>
<p class="abs post-text" style="left:600px">Uncover many web sites still in their infancy various versions...</p>
<p class="abs post-text" style="left:814px">Uncover many web sites still in their infancy various versions...</p>

<!-- ads -->
<div class="abs ad" style="left:294px;background:linear-gradient(135deg,#f2c35a,#e6a43a 45%,#8a8a8a)" role="img" aria-label="Bank advertisement banner"></div>
<div class="abs ad" style="left:618px;background:linear-gradient(160deg,#1f9bd6,#0f4f9c 60%,#0a2f66)" role="img" aria-label="Dive travel holiday advertisement banner"></div>

<!-- about -->
<div class="abs about"></div>
<h2 class="abs sec-title" style="top:2358px">ABOUT SKYWARD LENSWORKS</h2>
<p class="abs sec-text" style="left:245px;top:2409px;width:710px">It is a long established fact that a reader will be distracted by the readable content of a page when looking at its layout. The point of using Lorem Ipsum is that it has a more-or-less normal distribution of letters...</p>
<div class="abs btn btn-accent btn-small" style="left:421px;top:2484px;width:170px">LOGIN HERE</div>
<div class="abs btn btn-accent btn-small" style="left:609px;top:2484px;width:170px">REGISTER HERE</div>

<!-- footer -->
<footer class="abs footer"></footer>
<div class="abs foot-links">SEARCH<span>/</span>CALENDAR<span>/</span>ABOUT<span>/</span>DONATION<span>/</span>PRIVACY</div>
<div class="abs copy">COPYRIGHT. SKYWARD LENSWORKS (C) - ALL RIGHTS RESERVED.</div>
<div class="abs social" style="left:895px"></div>
<div class="abs social" style="left:942px"></div>
<div class="abs social" style="left:988px"></div>

</body>
</html>
```